My colors are BLACK, WHITE AND RED. I want something super professional but feminine and a bit sassy. My original logo is gold and black, I would like to see the crown in red (still with gradient) . I have a suggested layout in the files but am totally open to fresh ideas. I'm torn about having a little crown on the front as well as large logo on the back.

Target Market(s)

People buying high end houses

Font styles to use
Serif
Sans Serif

Requirements
Must have
• all the verbiage and text needed is on the business card in the files.
Nice to have
• classy, pretty, elegant, business like
Should not have
• cheesy, guady, boring

```html
<!DOCTYPE html>
<html lang="en">
<head>
<meta charset="utf-8">
<title>Vivian Ashford – Business Card</title>
<link rel="stylesheet" href="https://fonts.googleapis.com/css2?family=Cinzel:wght@400;600&family=Roboto:wght@400;500&display=swap">
<style>
  :root {
    --page-bg: #d9d9d9;
    --card-bg: #ffffff;
    --ink-dark: #3a3a38;
    --ink-mid: #6f6f6d;
    --ink-body: #4a4a48;
    --ink-black: #1a1a1a;
    --accent-red: #c8102e;
    --accent-red-deep: #7d0a1c;
    --accent-red-light: #e8404f;
    --photo-top: #c9c2bb;
    --photo-bottom: #2e2e30;
  }
  * { margin: 0; padding: 0; box-sizing: border-box; }
  html, body { width: 1200px; height: 1200px; overflow: hidden; }
  body {
    background: var(--page-bg);
    font-family: "Roboto", Arial, sans-serif;
    position: relative;
  }
  .card {
    position: absolute;
    left: 257px;
    width: 686px;
    height: 392px;
    background: var(--card-bg);
    box-shadow: 0 18px 30px rgba(0,0,0,0.28);
    overflow: hidden;
  }
  .card--front { top: 165px; }
  .card--back { top: 653px; }

  .portrait {
    position: absolute;
    left: 55px;
    top: 26px;
    width: 240px;
    height: 366px;
    border-radius: 110px 110px 0 0;
    background: linear-gradient(180deg, var(--photo-top) 0%, #8a6f5a 30%, var(--photo-bottom) 70%);
  }
  .front-info {
    position: absolute;
    right: 34px;
    top: 0;
    text-align: right;
    color: var(--ink-body);
  }
  .agent-name {
    position: absolute; right: 0; top: 42px;
    white-space: nowrap;
    font-size: 26px; font-weight: 500; color: var(--ink-dark); letter-spacing: 0.5px;
  }
  .agent-title {
    position: absolute; right: 0; top: 74px;
    white-space: nowrap;
    font-size: 18px; color: var(--ink-mid); letter-spacing: 0.6px;
  }
  .brokerage {
    position: absolute; right: 0; top: 188px;
    white-space: nowrap;
    font-size: 16.5px; font-weight: 500; color: var(--ink-dark);
  }
  .contact {
    position: absolute; right: 0; top: 216px;
    list-style: none;
    font-size: 16.5px; color: var(--ink-body);
  }
  .contact li {
    display: flex; justify-content: flex-end; align-items: center;
    gap: 14px; height: 23px; white-space: nowrap;
  }
  .contact svg { width: 14px; height: 14px; fill: var(--ink-dark); }
  .credentials {
    position: absolute; right: 0; top: 276px;
    list-style: none;
    font-size: 17px; line-height: 24.5px; color: var(--ink-body);
    white-space: nowrap;
  }

  .brand-mark {
    position: absolute;
    left: 303px; top: 92px;
    width: 80px; height: 80px;
    border-radius: 50%;
    background: linear-gradient(160deg, var(--accent-red-light) 0%, var(--accent-red) 50%, var(--accent-red-deep) 100%);
  }
  .back-brand {
    position: absolute; left: 0; right: 0; top: 196px;
    text-align: center;
    font-family: "Cinzel", Georgia, serif;
    font-weight: 600;
    font-size: 30px;
    letter-spacing: 9px;
    padding-left: 9px;
    color: var(--ink-black);
  }
  .award {
    position: absolute; left: 0; right: 0; top: 266px;
    text-align: center;
    font-family: "Cinzel", Georgia, serif;
    font-size: 23px; color: var(--ink-black); letter-spacing: 1px;
  }
  .award-sub {
    position: absolute; left: 0; right: 0; top: 299px;
    text-align: center;
    font-size: 14px; color: var(--ink-body); letter-spacing: 0.3px;
  }
  .office-line {
    position: absolute; left: 72px; top: 341px;
    font-size: 9.5px; color: var(--ink-body); white-space: nowrap;
  }
  .housing-badge {
    position: absolute; left: 601px; top: 330px;
    width: 32px; height: 32px;
    background: var(--ink-black);
  }
</style>
</head>
<body>
  <section class="card card--front">
    <div class="portrait" role="img" aria-label="Portrait photo of the agent in a black blazer, hand on hip"></div>
    <div class="front-info">
      <h1 class="agent-name">VIVIAN ASHFORD</h1>
      <p class="agent-title">REAL ESTATE AGENT</p>
      <p class="brokerage">SUMMIT CREST REALTY</p>
      <ul class="contact">
        <li>720-555-0148
          <svg viewBox="0 0 24 24" aria-hidden="true"><path d="M6.6 10.8a15.1 15.1 0 0 0 6.6 6.6l2.2-2.2a1 1 0 0 1 1-.25 11.4 11.4 0 0 0 3.6.57 1 1 0 0 1 1 1V20a1 1 0 0 1-1 1A17 17 0 0 1 3 4a1 1 0 0 1 1-1h3.5a1 1 0 0 1 1 1c0 1.25.2 2.45.57 3.57a1 1 0 0 1-.25 1z"/></svg>
        </li>
        <li>vashford@summitcrest.net
          <svg viewBox="0 0 24 24" aria-hidden="true"><path d="M2 5h20v14H2z M3.5 6.5 12 13l8.5-6.5" fill="var(--ink-dark)" stroke="#fff" stroke-width="1.4"/></svg>
        </li>
      </ul>
      <ul class="credentials">
        <li>Certified Mountain Area Specialist</li>
        <li>Certified Luxury Home Marketing Specialist</li>
        <li>Certified Negotiation Expert</li>
      </ul>
    </div>
  </section>

  <section class="card card--back">
    <div class="brand-mark" aria-hidden="true"></div>
    <p class="back-brand">VIVIAN ASHFORD</p>
    <p class="award">Summit Club Award 2018</p>
    <p class="award-sub">TOP PRODUCING INDIVIDUAL AGENT, ASPEN FALLS OFFICE 2018</p>
    <p class="office-line">1200 Ridgeline Rd. Aspen Falls, CO 80000 303-555-0190 &nbsp;Each office independently owned and operated</p>
    <div class="housing-badge" role="img" aria-label="Equal housing badge"></div>
  </section>
</body>
</html>
```